The Quiet Orchard of Copper Lanterns - 40-Week Tide Ledger

I am finishing a book that is designed to be super hands on. It steps he reader through a 90 day roadmap - as a pick up, put down action diary style piece. The foundational idea is to speak about the Quiet Orchard of Copper Lanterns. With a cost of living crisis this is designed to create action and understanding. I am looking for a cover for the ebook that will blow away the competitors in the category. I want it to be bright, attractive and leap off the lumora page - appeal to a wide audience. I have pasted in a file with the best selling books in the category so you can see what's working.

```html
<!DOCTYPE html>
<html lang="en">
<head>
<meta charset="utf-8">
<title>The Quiet Orchard of Copper Lanterns – 40-Week Tide Ledger</title>
<link rel="stylesheet" href="https://fonts.googleapis.com/css2?family=Oswald:wght@400;500;700&display=swap">
<style>
  :root {
    --navy-deep: #022659;
    --navy-mid: #033b85;
    --blue-glow: #0562d2;
    --stripe: #0656b8;
    --gold: #fcc918;
    --white: #ffffff;
    --ink: #000000;
  }
  html, body {
    margin: 0;
    padding: 0;
    width: 800px;
    height: 1200px;
    overflow: hidden;
    background: var(--navy-deep);
  }
  .book-cover {
    display: block;
    width: 800px;
    height: 1200px;
  }
  .glow-start { stop-color: var(--blue-glow); }
  .glow-mid { stop-color: var(--navy-mid); }
  .glow-end { stop-color: var(--navy-deep); }
  .stripe-solid { stop-color: var(--stripe); stop-opacity: 1; }
  .stripe-clear { stop-color: var(--stripe); stop-opacity: 0; }

  .word {
    font-family: "Oswald", "Arial Narrow", sans-serif;
    font-weight: 700;
  }
  .word-light {
    font-family: "Oswald", "Arial Narrow", sans-serif;
    font-weight: 400;
    fill: var(--white);
  }
  .extrude use {
    fill: var(--ink);
    stroke: var(--ink);
    stroke-width: 14;
    stroke-linejoin: round;
  }
  .face {
    fill: var(--gold);
    stroke: var(--white);
    stroke-width: 6;
    stroke-linejoin: miter;
    paint-order: stroke fill;
  }
  .rule {
    stroke: var(--white);
    stroke-width: 1.2;
    opacity: 0.85;
  }
  .subtitle {
    font-family: "Oswald", "Arial Narrow", sans-serif;
    font-weight: 500;
    fill: var(--gold);
  }
</style>
</head>
<body>
<svg class="book-cover" viewBox="0 0 800 1200" xmlns="http://www.w3.org/2000/svg" role="img" aria-label="The Quiet Orchard of Copper Lanterns – 40-Week Tide Ledger">
  <defs>
    <radialGradient id="bg-glow" cx="430" cy="530" r="720" gradientUnits="userSpaceOnUse">
      <stop offset="0" class="glow-start"/>
      <stop offset="0.45" class="glow-mid"/>
      <stop offset="1" class="glow-end"/>
    </radialGradient>
    <linearGradient id="stripe-left" x1="0" y1="0" x2="1" y2="0">
      <stop offset="0" class="stripe-solid"/>
      <stop offset="1" class="stripe-clear"/>
    </linearGradient>
    <linearGradient id="stripe-right" x1="0" y1="0" x2="1" y2="0">
      <stop offset="0" class="stripe-clear"/>
      <stop offset="1" class="stripe-solid"/>
    </linearGradient>

    <text id="line-quiet" class="word" x="40" y="360" font-size="160" textLength="730" lengthAdjust="spacingAndGlyphs">QUIET ORCHARD</text>
    <text id="line-copper" class="word" x="68" y="709" font-size="180" textLength="680" lengthAdjust="spacingAndGlyphs">COPPER</text>
    <text id="line-lanterns" class="word" x="70" y="898" font-size="205" textLength="680" lengthAdjust="spacingAndGlyphs">LANTERNS</text>
  </defs>

  <!-- background -->
  <rect class="backdrop" width="800" height="1200" fill="url(#bg-glow)"/>

  <!-- upper stripe band -->
  <g class="stripes stripes-upper">
    <rect x="0" y="64" width="300" height="11" fill="url(#stripe-left)"/>
    <rect x="0" y="87" width="300" height="11" fill="url(#stripe-left)"/>
    <rect x="0" y="110" width="300" height="11" fill="url(#stripe-left)"/>
    <rect x="0" y="133" width="300" height="11" fill="url(#stripe-left)"/>
    <rect x="0" y="156" width="300" height="11" fill="url(#stripe-left)"/>
    <rect x="0" y="179" width="300" height="11" fill="url(#stripe-left)"/>
    <rect x="500" y="64" width="300" height="11" fill="url(#stripe-right)"/>
    <rect x="500" y="87" width="300" height="11" fill="url(#stripe-right)"/>
    <rect x="500" y="110" width="300" height="11" fill="url(#stripe-right)"/>
    <rect x="500" y="133" width="300" height="11" fill="url(#stripe-right)"/>
    <rect x="500" y="156" width="300" height="11" fill="url(#stripe-right)"/>
    <rect x="500" y="179" width="300" height="11" fill="url(#stripe-right)"/>
  </g>

  <!-- middle stripe band -->
  <g class="stripes stripes-middle">
    <rect x="0" y="402" width="250" height="11" fill="url(#stripe-left)"/>
    <rect x="0" y="425" width="250" height="11" fill="url(#stripe-left)"/>
    <rect x="0" y="448" width="250" height="11" fill="url(#stripe-left)"/>
    <rect x="0" y="471" width="250" height="11" fill="url(#stripe-left)"/>
    <rect x="0" y="494" width="250" height="11" fill="url(#stripe-left)"/>
    <rect x="0" y="517" width="250" height="11" fill="url(#stripe-left)"/>
    <rect x="550" y="402" width="250" height="11" fill="url(#stripe-right)"/>
    <rect x="550" y="425" width="250" height="11" fill="url(#stripe-right)"/>
    <rect x="550" y="448" width="250" height="11" fill="url(#stripe-right)"/>
    <rect x="550" y="471" width="250" height="11" fill="url(#stripe-right)"/>
    <rect x="550" y="494" width="250" height="11" fill="url(#stripe-right)"/>
    <rect x="550" y="517" width="250" height="11" fill="url(#stripe-right)"/>
  </g>

  <!-- title -->
  <g class="title">
    <text class="word-light title-the" x="392" y="179" font-size="130" text-anchor="middle" textLength="164" lengthAdjust="spacingAndGlyphs">THE</text>

    <g class="title-line">
      <g class="extrude">
        <use href="#line-quiet"/>
        <use href="#line-quiet" transform="translate(-4 4)"/>
        <use href="#line-quiet" transform="translate(-8 8)"/>
        <use href="#line-quiet" transform="translate(-12 12)"/>
        <use href="#line-quiet" transform="translate(-16 16)"/>
      </g>
      <use href="#line-quiet" class="face"/>
    </g>

    <text class="word-light title-of" x="392" y="518" font-size="130" text-anchor="middle" textLength="94" lengthAdjust="spacingAndGlyphs">OF</text>

    <g class="title-line">
      <g class="extrude">
        <use href="#line-copper"/>
        <use href="#line-copper" transform="translate(-4 4)"/>
        <use href="#line-copper" transform="translate(-8 8)"/>
        <use href="#line-copper" transform="translate(-12 12)"/>
        <use href="#line-copper" transform="translate(-16 16)"/>
        <use href="#line-copper" transform="translate(-20 20)"/>
      </g>
      <use href="#line-copper" class="face"/>
    </g>

    <g class="title-line">
      <g class="extrude">
        <use href="#line-lanterns"/>
        <use href="#line-lanterns" transform="translate(-4 4)"/>
        <use href="#line-lanterns" transform="translate(-8 8)"/>
        <use href="#line-lanterns" transform="translate(-12 12)"/>
        <use href="#line-lanterns" transform="translate(-16 16)"/>
        <use href="#line-lanterns" transform="translate(-20 20)"/>
      </g>
      <use href="#line-lanterns" class="face"/>
    </g>
  </g>

  <!-- subtitle -->
  <g class="subtitle-block">
    <line class="rule" x1="106" y1="1002" x2="688" y2="1002"/>
    <text class="subtitle" x="106" y="1085" font-size="82" textLength="584" lengthAdjust="spacingAndGlyphs">40-Week Tide Ledger</text>
    <line class="rule" x1="106" y1="1113" x2="688" y2="1113"/>
  </g>
</svg>
</body>
</html>
```